Business Card Design Project

for a second hand vintage clothing store. shop name is The Velvet Cupboard

Cards to be double sided

The name on the card is Joanna Whitfield

Information to put on card:

The Velvet Cupboard
Joanna Whitfield (no job title)
42/871 Dunmore St, Glenwick, Sydney, NSW, 2009.
Mobile: 0412 905 261
Email: thevelvetcupboard@mailbox.com.au
Web: www.thevelvetcupboard.com.au

Target Market(s)

Women looking at vintage clothing

Industry/Entity Type

Clothing

```html
<!DOCTYPE html>
<html lang="en">
<head>
<meta charset="utf-8">
<title>The Velvet Cupboard – Business Card</title>
<link rel="stylesheet" href="https://fonts.googleapis.com/css2?family=Quicksand:wght@300;400;500&display=swap">
<style>
  :root {
    --card-bg: #000000;
    --ink-white: #ffffff;
    --ink-gold: #ead59a;
    --ink-gold-bright: #e6c66e;
    --ink-grey: #9a9a9a;
    --ink-red: #a3181a;
  }

  html, body {
    margin: 0;
    padding: 0;
    width: 1200px;
    height: 600px;
    overflow: hidden;
    background: var(--card-bg);
  }

  .card {
    position: relative;
    width: 1200px;
    height: 600px;
    background: var(--card-bg);
    font-family: "Quicksand", sans-serif;
    color: var(--ink-white);
    overflow: hidden;
  }

  .card > * {
    position: absolute;
    margin: 0;
    line-height: 1;
    white-space: nowrap;
  }

  .brand-name {
    top: 100px;
    right: 82px;
    font-size: 44px;
    font-weight: 400;
    letter-spacing: 0.02em;
    color: var(--ink-gold);
  }

  .person-name {
    top: 326px;
    left: 45px;
    font-size: 46px;
    font-weight: 400;
    letter-spacing: 0.14em;
  }

  .person-name .first { color: var(--ink-white); }
  .person-name .last  { color: var(--ink-gold); }

  .website {
    top: 384px;
    left: 290px;
    font-size: 16px;
    font-weight: 500;
    color: var(--ink-white);
  }

  .email {
    top: 432px;
    left: 55px;
    font-size: 17px;
    font-weight: 400;
  }

  .email .user   { color: var(--ink-grey); }
  .email .domain { color: var(--ink-gold-bright); }

  .phone {
    top: 480px;
    left: 55px;
    font-size: 32px;
    font-weight: 300;
    letter-spacing: 0.2em;
    color: var(--ink-white);
  }

  .phone .country-code { color: var(--ink-red); }

  .address {
    top: 540px;
    left: 55px;
    font-size: 16px;
    font-weight: 400;
    color: var(--ink-grey);
  }
</style>
</head>
<body>
  <main class="card">
    <p class="brand-name">The Velvet Cupboard</p>

    <h1 class="person-name"><span class="first">Joanna</span> <span class="last">Whitfield</span></h1>
    <p class="website">www.thevelvetcupboard.com.au</p>

    <p class="email"><span class="user">thevelvetcupboard</span><span class="domain">@mailbox.com.au</span></p>
    <p class="phone"><span class="country-code">(+61)</span>0412 905 261</p>
    <p class="address">42/871 Dunmore St, Glenwick, Sydney, NSW, 2009</p>
  </main>
</body>
</html>
```